Residential Construction Company needs flyer designed.

We need a flyer design for a residential Rain Gutter and Screen room company. We have over 50 years in the remodeling industry and service all of Middle Georgia. We want the brochure to highlight our wonderful managerial staff to our great instillation crews. We also want to showcase the high-quality products that we use, gutter, leaf protection, screen rooms and sunrooms and the quality craftsmanship homeowners will receive when they choose to go with our company.

```html
<!DOCTYPE html>
<html lang="en">
<head>
<meta charset="utf-8">
<title>Hartwell Gutters &amp; Exteriors Flyer</title>
<link href="https://fonts.googleapis.com/css2?family=Poppins:wght@400;600;700;800&display=swap" rel="stylesheet">
<style>
:root{
  --teal:#1f9e95;
  --teal-dark:#0f6f78;
  --purple:#2e2a6e;
  --purple-mid:#3a3585;
  --ink:#1d1d28;
  --white:#ffffff;
  --page:#e8eaed;
  --photo-a:#b9c4c9;
  --photo-b:#8d9aa2;
}
*{box-sizing:border-box;margin:0;padding:0}
html,body{width:1200px;height:787px;overflow:hidden;background:var(--page);font-family:'Poppins',sans-serif}
.flyer{position:absolute;left:342px;top:30px;width:515px;height:728px;background:var(--white);overflow:hidden;box-shadow:0 4px 14px rgba(0,0,0,.18)}
.hero-photo{position:absolute;left:0;top:0;width:515px;height:380px;background:linear-gradient(160deg,#c7d2d3 0%,#a7b3b5 45%,#8f7f6b 100%)}
.hero-tint{position:absolute;left:0;top:0;width:515px;height:380px;background:linear-gradient(90deg,var(--teal) 0%,rgba(31,158,149,.85) 40%,rgba(31,158,149,0) 75%)}
.shapes{position:absolute;left:0;top:0}
.brand{position:absolute;left:350px;top:40px;width:135px;font-weight:800;font-size:15px;line-height:1.1;color:var(--purple);display:flex;align-items:center;gap:6px}
.brand-dot{width:12px;height:12px;border-radius:50%;background:var(--purple);flex:none}
.title{position:absolute;left:26px;top:26px;color:var(--white);font-weight:800;font-size:39px;line-height:40px;letter-spacing:.5px}
.tagline{position:absolute;left:26px;top:155px;color:var(--white);font-weight:400;font-size:22px;line-height:23px}
.spec-heading{position:absolute;left:26px;top:332px;color:var(--purple);font-weight:700;font-size:17px;line-height:20px}
.rule{position:absolute;left:0;top:382px;width:305px;height:1px;background:var(--teal)}
.services{position:absolute;left:24px;top:404px;list-style:none}
.services li{display:flex;align-items:center;gap:12px;height:26px;font-size:12.5px;color:var(--ink)}
.finance{position:absolute;left:180px;top:470px;width:150px;height:64px}
.finance-text{position:absolute;left:0;top:6px;width:146px;text-align:center;color:var(--white)}
.finance-kicker{font-size:7.5px;letter-spacing:.3px}
.finance-main{font-weight:700;font-size:15.5px;line-height:17px}
.badge{position:absolute;left:156px;top:547px;width:42px;height:42px;border-radius:50%;background:#d9dde3;border:3px solid #6d7380}
.partners{position:absolute;left:47px;top:609px;width:261px;height:55px;border:1px solid var(--purple);border-bottom:none}
.partners-label{position:absolute;left:50%;top:-10px;transform:translateX(-50%);background:var(--purple);color:var(--white);font-size:11px;padding:0 4px;line-height:15px;white-space:nowrap}
.partner-row{position:absolute;left:0;top:18px;width:100%;height:37px;display:flex}
.partner{flex:1;display:flex;align-items:center;justify-content:center;font-weight:700;font-size:9.5px;color:var(--purple);border-right:1px solid var(--purple)}
.partner:last-child{border-right:none}
.footer{position:absolute;left:0;top:667px;width:356px;height:41px;background:var(--purple);color:var(--white)}
.footer-label{position:absolute;top:4px;font-size:10px}
.footer-phone{position:absolute;left:21px;top:17px;font-weight:700;font-size:13px}
.footer-address{position:absolute;left:136px;top:21px;font-weight:700;font-size:8.3px}
.footer-strip{position:absolute;left:0;top:708px;width:356px;height:20px;background:var(--teal);color:var(--white)}
.social{position:absolute;top:5px;width:10px;height:10px;border-radius:2px;background:var(--white)}
.email{position:absolute;left:136px;top:3px;font-size:9px}
</style>
</head>
<body>
<div class="flyer">
  <div class="hero-photo" role="img" aria-label="Photo of a small model house with a grey roof on a wooden table"></div>
  <div class="hero-tint"></div>

  <svg class="shapes" width="515" height="728" viewBox="0 0 515 728">
    <defs>
      <linearGradient id="bandPurple" x1="0" x2="1"><stop offset="0" stop-color="#2e2a6e"/><stop offset="1" stop-color="#3a3585"/></linearGradient>
      <linearGradient id="bandTeal" x1="0" x2="1"><stop offset="0" stop-color="#1f9e95"/><stop offset="1" stop-color="#2b5f88"/></linearGradient>
      <linearGradient id="guard" x1="0" y1="0" x2="1" y2="1"><stop offset="0" stop-color="#7e9a5a"/><stop offset="1" stop-color="#6d7278"/></linearGradient>
      <linearGradient id="sunroom" x1="0" y1="0" x2="0" y2="1"><stop offset="0" stop-color="#e6e9ec"/><stop offset="1" stop-color="#4f7a44"/></linearGradient>
      <linearGradient id="screenroom" x1="0" y1="0" x2="0" y2="1"><stop offset="0" stop-color="#8a8f98"/><stop offset="1" stop-color="#a59a8c"/></linearGradient>
      <linearGradient id="bubble" x1="0" x2="1"><stop offset="0" stop-color="#1f9e95"/><stop offset="1" stop-color="#0f4f6e"/></linearGradient>
    </defs>
    <path d="M0,276 L515,354 V728 H0 Z" fill="#ffffff"/>
    <g role="img" aria-label="Photo of perforated gutter guard on a shingle roof">
      <path d="M356,320 H515 V446 L356,422 Z" fill="url(#guard)"/>
    </g>
    <g role="img" aria-label="Photo of a white sunroom with garden shrubs">
      <path d="M356,426 L515,450 V606 L356,556 Z" fill="url(#sunroom)"/>
    </g>
    <g role="img" aria-label="Photo of a brick screen room with an arched opening">
      <path d="M356,560 L515,610 V728 H356 Z" fill="url(#screenroom)"/>
    </g>
    <path d="M0,246 L440,330 L515,354 L0,276 Z" fill="url(#bandTeal)"/>
    <path d="M0,236 L440,300 Q508,310 515,354 L440,330 L0,246 Z" fill="url(#bandPurple)"/>
  </svg>

  <div class="brand"><span class="brand-dot"></span>HARTWELL GUTTERS &amp; EXTERIORS</div>

  <h1 class="title">HARTWELL<br>GUTTERS &amp;<br>EXTERIORS</h1>
  <p class="tagline">Offer Unparalleled<br>Home Improvement<br>Service</p>

  <h2 class="spec-heading">We specializes<br>in the quality installation of:</h2>
  <div class="rule"></div>

  <ul class="services">
    <li><svg width="14" height="14" viewBox="0 0 14 14"><circle cx="7" cy="7" r="6" fill="none" stroke="#1f9e95" stroke-width="1.3"/><path d="M4,7.2 L6.2,9.2 L10,5" fill="none" stroke="#1f9e95" stroke-width="1.4"/></svg>FlowGuard Gutter Protection System</li>
    <li><svg width="14" height="14" viewBox="0 0 14 14"><circle cx="7" cy="7" r="6" fill="none" stroke="#1f9e95" stroke-width="1.3"/><path d="M4,7.2 L6.2,9.2 L10,5" fill="none" stroke="#1f9e95" stroke-width="1.4"/></svg>Seamless Aluminum Gutters &amp; Downspouts</li>
    <li><svg width="14" height="14" viewBox="0 0 14 14"><circle cx="7" cy="7" r="6" fill="none" stroke="#1f9e95" stroke-width="1.3"/><path d="M4,7.2 L6.2,9.2 L10,5" fill="none" stroke="#1f9e95" stroke-width="1.4"/></svg>Gutter Cleaning</li>
    <li><svg width="14" height="14" viewBox="0 0 14 14"><circle cx="7" cy="7" r="6" fill="none" stroke="#1f9e95" stroke-width="1.3"/><path d="M4,7.2 L6.2,9.2 L10,5" fill="none" stroke="#1f9e95" stroke-width="1.4"/></svg>Patio Covers</li>
    <li><svg width="14" height="14" viewBox="0 0 14 14"><circle cx="7" cy="7" r="6" fill="none" stroke="#1f9e95" stroke-width="1.3"/><path d="M4,7.2 L6.2,9.2 L10,5" fill="none" stroke="#1f9e95" stroke-width="1.4"/></svg>Gutter Covers</li>
  </ul>

  <div class="finance">
    <svg width="150" height="64" viewBox="0 0 150 64"><path d="M10,2 H142 Q149,2 148,10 L144,52 Q143,58 136,58 H18 Q10,58 6,64 Q4,56 3,48 L2,10 Q2,2 10,2 Z" fill="url(#bubble)"/></svg>
    <div class="finance-text">
      <div class="finance-kicker">FINANCE YOUR PROJECT</div>
      <div class="finance-main">Quick &amp; Easy<br>0% Financing</div>
    </div>
  </div>

  <div class="badge"></div>

  <div class="partners">
    <span class="partners-label">Our Partners</span>
    <div class="partner-row">
      <div class="partner">VALEVIEW</div>
      <div class="partner">SCREENLINE</div>
      <div class="partner">FLOWGUARD</div>
      <div class="partner">ARCHWAY</div>
    </div>
  </div>

  <div class="footer">
    <span class="footer-label" style="left:21px">Contact Us:</span>
    <span class="footer-label" style="left:136px">Location:</span>
    <span class="footer-phone">(478) 555-0142</span>
    <span class="footer-address">214 Magnolia Ridge Rd, Perry, GA 31069</span>
  </div>
  <div class="footer-strip">
    <span class="social" style="left:21px"></span>
    <span class="social" style="left:39px"></span>
    <span class="email">info@hartwellgutters-ga.com</span>
  </div>
</div>
</body>
</html>
```